Welbourne Dental, P.C. New stationary and business card for modern Dental Office

We need a new stationary/envelope/business card design using our newly designed logo. We are looking for an upscale look. Our new logo is used on our signage, using black as the background and white for the lettering. We would like the stationary to have black, white, possible greys or silver. We are looking for a letterhead, envelope, and business card design for three different employees, as well as a 4th card, same design, but just general with no employee name.

Project Deadline Extended
Reason: We began this project in the middle of our move into our new office. Things got pretty hectic and we just didn't have the time to go through designs. We now settled in and finally eliminated the designs that didn't work for us. We would like to extend the project another 5 days, and then finalize our decision. Most of the submissions showed business cards alone, with no stationary designs. Our original request was for stationary and business cards. Please keep this in mind.

Target Market(s)

Dental patients expecting high quality, cosmetic dentistry

Industry/Entity Type

Business

Contact Information for Business Card

Will need a design using our logo. All cards will be the same, other than that one card will have Office Managers name, One for the Doctor, Hygienist,
1. Office Manager - Marisol Dubrovka
2. Hygienist - Kayleigh Morrow
3. Gordon T. Welbourne, D.D.S.
4. One general one with no staff names

Font styles to use
Other font styles liked:
• see upload

Colors
000000
1b1b1b
757575
c9c9c9
e8e8e8
ffffff

Requirements
Must have
• -Logo
• -Phone number (718)555-0193
• -Address: 4352 63rd Ave
• Lower Level
• Brooklyn, NY 11290

```html
<!DOCTYPE html>
<html lang="en">
<head>
<meta charset="utf-8">
<title>Welbourne Dental, P.C. — Stationery</title>
<link href="https://fonts.googleapis.com/css2?family=Lato:wght@400;700&display=swap" rel="stylesheet">
<style>
  :root {
    --black: #000000;
    --ink: #1b1b1b;
    --grey: #757575;
    --silver: #c9c9c9;
    --mist: #e8e8e8;
    --white: #ffffff;
    --sheet-w: 400px;
    --sheet-h: 566px;
  }
  * { box-sizing: border-box; margin: 0; padding: 0; }
  html, body { width: 1200px; height: 720px; overflow: hidden; }
  body {
    background: var(--mist);
    font-family: "Lato", sans-serif;
    color: var(--ink);
    position: relative;
  }
  .sheet {
    position: absolute;
    top: 77px;
    width: var(--sheet-w);
    height: var(--sheet-h);
    box-shadow: 0 6px 18px rgba(0,0,0,0.18);
  }
  .letterhead { left: 170px; background: #f7f7f7; }
  .cover { left: 630px; background: var(--ink); overflow: hidden; }

  .brand {
    display: flex;
    align-items: center;
    justify-content: center;
    gap: 8px;
  }
  .brand-name {
    font-family: "Lato", sans-serif;
    font-weight: 700;
    letter-spacing: 0.02em;
  }
  .brand-dot {
    border-radius: 50%;
    border: 1.5px solid currentColor;
  }
  .letterhead .brand { position: absolute; top: 44px; left: 0; right: 0; color: var(--grey); }
  .letterhead .brand-name { font-size: 16px; }
  .letterhead .brand-dot { width: 14px; height: 14px; }

  .letter {
    position: absolute;
    left: 44px;
    right: 44px;
    top: 122px;
    font-size: 7.5px;
    line-height: 1.45;
    color: var(--ink);
  }
  .recipient { margin-left: 8px; margin-bottom: 18px; }
  .letter p.body { margin-bottom: 12px; }
  .signoff { margin-top: 34px; }

  .footer-band {
    position: absolute;
    left: 0; right: 0;
    bottom: 48px;
    height: 16px;
    background: var(--black);
    display: flex;
    align-items: center;
    justify-content: center;
    gap: 22px;
    color: var(--silver);
    font-size: 6.5px;
  }
  .footer-item { display: flex; align-items: center; gap: 5px; }
  .footer-item svg { width: 7px; height: 7px; fill: var(--silver); }
  .footer-rule {
    position: absolute;
    left: 0; right: 0;
    bottom: 40px;
    height: 3px;
    background: var(--black);
  }

  .cover-texture {
    position: absolute;
    inset: 0;
    background: radial-gradient(circle at 50% 50%, #262626 0%, var(--ink) 70%);
  }
  .cover .brand { position: absolute; top: 0; bottom: 0; left: 0; right: 0; color: var(--silver); }
  .cover .brand-name { font-size: 20px; }
  .cover .brand-dot { width: 18px; height: 18px; }
</style>
</head>
<body>

  <section class="sheet letterhead" aria-label="Letterhead">
    <div class="brand">
      <span class="brand-name">Welbourne Dental, P.C.</span>
      <span class="brand-dot"></span>
    </div>

    <div class="letter">
      <p class="recipient">
        Mr. Daniel Crane<br>
        Managing Director<br>
        Northway Capital<br>
        210 W Oak Street<br>
        USA
      </p>
      <p class="body">Lorem Ipsum is simply dummy text of the printing and typesetting industry. Lorem Ipsum has been the industry's standard dummy text since the 1500s, when an unknown printer took a galley of type and scrambled it to make a type specimen book. Release of Letraset sheets containing Lorem Ipsum passages and more recently with desktop publishing software like Aldus PageMaker including version 6.9 of Lorem Ipsum.</p>
      <p class="body">Lorem Ipsum is simply dummy text for printing and typesetting industry. Lorem Ipsum has been the industry's standard dummy text since the 1500s, when an unknown printer took a galley and scrambled it to make a type specimen book. Release of Letraset sheets containing Lorem Ipsum passages and more recently with desktop publishing software like Aldus PageMaker including version 6.9 of Lorem Ipsum.</p>
      <p class="body">Contrary to popular belief, Lorem Ipsum is not simply random text. It has roots in a piece of classical Latin literature from 45 BC, making it over 2000 years old. A Latin professor at a small college in Virginia looked up one of the more obscure words, from a treatise on the theory of ethics very popular during the Renaissance.</p>
      <p class="body">Thank you for being one of our valued customers.</p>
      <p class="signoff">Name Here<br>CEO</p>
    </div>

    <div class="footer-band">
      <span class="footer-item">
        <svg viewBox="0 0 10 10" aria-hidden="true"><path d="M5 0a3.5 3.5 0 0 0-3.5 3.5C1.5 6 5 10 5 10s3.5-4 3.5-6.5A3.5 3.5 0 0 0 5 0zm0 5a1.5 1.5 0 1 1 0-3 1.5 1.5 0 0 1 0 3z"/></svg>
        4352 63rd Ave, Lower Level Brooklyn, NY 11290
      </span>
      <span class="footer-item">
        <svg viewBox="0 0 10 10" aria-hidden="true"><path d="M2 0.5l2 2-1 1.2c.6 1.3 1.6 2.3 2.9 2.9l1.2-1 2 2-1.3 1.6C4 9 1 6 .4 1.8z"/></svg>
        (718) 555 0193
      </span>
    </div>
    <div class="footer-rule"></div>
  </section>

  <section class="sheet cover" aria-label="Letterhead reverse">
    <div class="cover-texture" role="img" aria-label="Dark embossed repeating pattern across the sheet"></div>
    <div class="brand">
      <span class="brand-name">Welbourne Dental, P.C.</span>
      <span class="brand-dot"></span>
    </div>
  </section>

</body>
</html>
```